Web Page Design for a Website that Provides Tutoring

I am looking to create an online tutoring website. The website will allow parents or students to contact tutors with a view to instructing them to tutor themselves or their children.

The name of the website is LendYourLessons.

This brief is to create the design for one of the web pages for this web site. I am hoping the same designer will be available to design other pages.

The page I want designed is one of the more complex and I have attached the design as an excel spreadsheet. The web page needs to include all the items on this page but if you want to change the positioning of the items then Im fine with that.

I recently had two logos created for this website. My favourite is the one with a mortar board but im not sure I like the colours. I have attached both of these logos and you can use either of them, change the colours or create something different. I just want a design pleasing to the eye. If the logo is changed I would like that in a seperate file.

So can you please submit designs for this page. I have attached the two logos which you can use, change or if you feel you have a better idea then you can use that.

On the spreadsheet the Send Message, Favourite etc are buttons.

Target Market(s)

People who want to better themselves.
Possible middle class to upper class.

Industry/Entity Type

Tutoring

Number of Pages Required

1 page

Requirements
Must have
• The designs must have alot of the information attached in the spreadsheet.

```html
<!DOCTYPE html>
<html lang="en">
<head>
<meta charset="utf-8">
<title>LendYourLessons – Tutoring</title>
<link href="https://fonts.googleapis.com/css2?family=Jost:wght@400;500&family=Lato:wght@400;700&family=Oswald:wght@400;500&display=swap" rel="stylesheet">
<style>
:root{
  --blue:#3b5c9c;
  --blue-dark:#2f4d86;
  --orange:#f26640;
  --ink:#333333;
  --muted:#555555;
  --rule:#c9c9c9;
  --grey-bg:#ececec;
  --footer:#323232;
  --table-head:#cdd5e1;
  --white:#ffffff;
}
*{box-sizing:border-box;margin:0;padding:0}
html,body{width:1200px;height:2403px;overflow:hidden}
body{position:relative;background:var(--white);font-family:"Lato",sans-serif;color:var(--ink)}
.abs{position:absolute}

/* top bar */
.topbar{left:0;top:0;width:1200px;height:30px;background:var(--blue);color:var(--white);font-size:13px}
.topbar .item{position:absolute;top:7px;display:flex;align-items:center;gap:8px}

/* header */
.header{left:0;top:30px;width:1200px;height:87px;background:var(--white)}
.brand{position:absolute;left:160px;top:52px;font-family:"Jost",sans-serif;font-weight:500;font-size:22px;color:var(--blue)}
.brand-mark{position:absolute;left:212px;top:12px;width:36px;height:36px;background:var(--orange);border-radius:4px}
.nav{position:absolute;top:38px;font-family:"Jost",sans-serif;font-size:12.5px;color:var(--ink);letter-spacing:.3px}
.nav.active{color:var(--orange)}
.login{position:absolute;left:953px;top:32px;width:85px;height:28px;background:var(--blue);color:var(--white);font-size:12px;display:flex;align-items:center;justify-content:center;gap:8px}

/* hero */
.hero{left:0;top:117px;width:1200px;height:442px;background:var(--blue)}
.hero-photo{position:absolute;left:0;top:0;width:650px;height:442px;background:linear-gradient(135deg,#e9dcc2 0%,#cdb98f 45%,#8e8a84 100%);clip-path:path("M0 0 H640 Q590 221 640 442 H0 Z")}
.hero-edge{position:absolute;left:0;top:0}
.hero-text{position:absolute;left:643px;top:280px;width:400px;text-align:center;font-family:"Oswald",sans-serif;font-size:28px;line-height:37px;color:var(--white);letter-spacing:.5px}
.btn-start{position:absolute;left:767px;top:404px;width:173px;height:38px;background:var(--orange);color:var(--white);font-family:"Oswald",sans-serif;font-size:16px;display:flex;align-items:center;justify-content:center}
.dots{position:absolute;left:825px;top:459px;display:flex;gap:6px}
.dots span{width:9px;height:9px;border-radius:50%;border:1.5px solid var(--white)}
.dots span.on{background:var(--white)}

/* section titles */
.title{position:absolute;font-family:"Jost",sans-serif;font-size:26px}
.title .o{color:var(--orange)}
.title .b{color:var(--blue)}
.divider{position:absolute;height:1px;background:var(--rule)}
.divider i{position:absolute;left:50%;top:-3px;width:7px;height:7px;background:var(--rule);transform:translateX(-50%) rotate(45deg)}

/* about */
.about-photo{left:162px;top:602px;width:147px;height:161px;background:var(--orange);padding:8px}
.about-photo .ph{width:100%;height:118px;background:linear-gradient(180deg,#e8eef6,#b9c7dc)}
.about-photo .cap{color:var(--white);font-size:10px;font-weight:700;text-align:center;margin-top:7px}
.about-text{left:341px;top:655px;width:698px;font-size:12px;line-height:21px;color:var(--muted)}
.btn{position:absolute;height:27px;color:var(--white);font-size:11.5px;display:flex;align-items:center;justify-content:center}
.btn.blue{background:var(--blue)}
.btn.orange{background:var(--orange)}

/* services */
.services-band{left:0;top:817px;width:1200px;height:295px;background:linear-gradient(120deg,#3a3430,#26231f 50%,#3b3733)}
.service-card{position:absolute;top:966px;width:244px;height:215px}
.service-card.orange{background:var(--orange)}
.service-card.grey{background:#e4e4e4}
.service-title{position:absolute;top:1204px;width:300px;text-align:center;font-family:"Jost",sans-serif;font-weight:500;font-size:14.5px;color:var(--ink)}
.service-text{position:absolute;top:1232px;width:240px;text-align:center;font-size:11.5px;line-height:19px;color:var(--muted)}
.arrow{position:absolute;top:1064px}

/* reviews */
.reviews-bg{left:0;top:1379px;width:1200px;height:358px;background:var(--grey-bg)}
.reviews-sub{left:0;top:1494px;width:1200px;text-align:center;font-size:15px;color:var(--ink)}
.review-table{position:absolute;left:162px;top:1535px;width:876px;border-collapse:collapse;background:#f6f6f6;border:1px solid #b9b9b9;font-size:14px}
.review-table th{height:38px;background:var(--table-head);font-family:"Jost",sans-serif;font-weight:400;font-size:16.5px;text-align:left;padding-left:65px;color:var(--ink);border-right:1px solid #b9b9b9}
.review-table th:nth-child(2),.review-table th:nth-child(3){padding-left:52px}
.review-table td{height:36px;padding-left:65px;color:var(--muted);border-right:1px solid #b9b9b9;border-top:1px solid #c9c9c9}
.review-table td:nth-child(2){padding-left:52px}
.review-table td:nth-child(3){padding-left:0;color:var(--blue);padding-left:2px}
.scroll{position:absolute;left:1031px;top:1573px;width:7px;height:109px;background:#dcdcdc}
.scroll i{position:absolute;left:0;top:38px;width:7px;height:25px;background:var(--blue)}

/* testimonial */
.quote{position:absolute;left:0;top:0}
.quote-text{left:185px;top:1864px;width:830px;text-align:center;font-size:11.5px;line-height:19px;color:var(--muted)}
.avatar{left:317px;top:1959px;width:56px;height:56px;border-radius:50%;border:2px solid var(--orange);background:linear-gradient(180deg,#e8eef6,#b9c7dc)}
.client-name{left:385px;top:1978px;font-size:13px;color:var(--orange)}
.client-city{left:516px;top:1979px;font-size:11.5px;color:var(--muted)}

/* footer */
.footer{left:0;top:2059px;width:1200px;height:301px;background:var(--footer);color:#e6e6e6}
.f-head{position:absolute;top:43px;font-family:"Jost",sans-serif;font-size:15.5px;color:var(--white);padding-bottom:10px;border-bottom:1px solid #5c5c5c}
.f-link{position:absolute;left:160px;font-size:11.5px}
.f-text{position:absolute;left:325px;font-size:11px;line-height:15px}
.f-icon{position:absolute;left:326px;font-size:12px;display:flex;align-items:center;gap:9px}
.f-input{position:absolute;left:569px;width:214px;background:var(--white);font-size:10px;color:#9a9a9a;padding:4px 6px}
.f-submit{position:absolute;left:569px;top:229px;width:85px;height:25px;background:var(--blue);color:var(--white);font-size:11px;display:flex;align-items:center;justify-content:center}
.f-brand{position:absolute;left:849px;top:180px;width:190px;text-align:center;font-family:"Jost",sans-serif;font-weight:500;font-size:22px;color:#c8c8c8}
.f-brand-mark{position:absolute;left:911px;top:92px;width:66px;height:66px;background:#9b9b9b;border-radius:4px}

/* bottom bar */
.bottombar{left:0;top:2360px;width:1200px;height:43px;background:var(--blue);color:var(--white);font-size:12px}
.social{position:absolute;top:7px;width:29px;height:29px;border-radius:50%;border:2px solid var(--white)}
.social.on{background:var(--orange);border-color:var(--orange)}
</style>
</head>
<body>

<!-- top bar -->
<div class="abs topbar">
  <div class="item" style="left:742px">
    <svg width="13" height="13" viewBox="0 0 24 24"><path fill="#fff" d="M6.6 10.8a15.1 15.1 0 0 0 6.6 6.6l2.2-2.2c.3-.3.7-.4 1-.2 1.1.4 2.3.6 3.6.6.6 0 1 .4 1 1V20c0 .6-.4 1-1 1A17 17 0 0 1 3 4c0-.6.4-1 1-1h3.5c.6 0 1 .4 1 1 0 1.3.2 2.5.6 3.6.1.3 0 .7-.2 1z"/></svg>
    <span>123 456 7890</span>
  </div>
  <div class="item" style="left:863px">
    <svg width="15" height="11" viewBox="0 0 20 14"><rect x="0.5" y="0.5" width="19" height="13" fill="#fff"/><path d="M1 1l9 7 9-7" stroke="#3b5c9c" stroke-width="1.5" fill="none"/></svg>
    <span>info@lendyourlessons.com</span>
  </div>
</div>

<!-- header -->
<header class="abs header">
  <div class="brand-mark"></div>
  <div class="brand">LendYourLessons</div>
  <nav>
    <span class="nav active" style="left:505px">HOME</span>
    <span class="nav" style="left:577px">ABOUT</span>
    <span class="nav" style="left:654px">STUDENT</span>
    <span class="nav" style="left:742px">TUTOR</span>
    <span class="nav" style="left:816px">CONTACT</span>
  </nav>
  <svg class="abs" style="left:921px;top:37px" width="17" height="17" viewBox="0 0 20 20"><circle cx="8" cy="8" r="6" stroke="#666" stroke-width="2" fill="none"/><path d="M12.5 12.5l5.5 5.5" stroke="#666" stroke-width="2.2"/></svg>
  <div class="login">
    <svg width="18" height="14" viewBox="0 0 18 14"><rect x="10" y="0" width="8" height="14" fill="#fff"/><path d="M0 7h8M5 3.5L8.5 7 5 10.5" stroke="#fff" stroke-width="2" fill="none"/></svg>
    <span>Login</span>
  </div>
</header>

<!-- hero -->
<section class="abs hero">
  <div class="hero-photo" role="img" aria-label="Photo of a young girl using a tablet in a classroom"></div>
  <svg class="hero-edge" width="660" height="442"><path d="M640 0 Q590 221 640 442" stroke="#f26640" stroke-width="4" fill="none"/></svg>
  <div class="hero-text">LEARN FROM<br>THE BEST AT YOUR<br>PACE &amp; YOUR CONVENIENCE</div>
  <div class="btn-start">START NOW</div>
  <div class="dots"><span class="on"></span><span></span><span></span><span></span></div>
</section>

<!-- about -->
<section>
  <div class="abs about-photo">
    <div class="ph" role="img" aria-label="Portrait of a tutor"></div>
    <div class="cap">Lorem Ipsum Dolor</div>
  </div>
  <h2 class="title" style="left:347px;top:598px"><span class="b">About</span> <span class="o">Lend Your Lessons</span></h2>
  <div class="divider" style="left:345px;top:643px;width:693px"></div>
  <p class="abs about-text">Lorem ipsum dolor sit amet, consectetuer adipiscing elit, sed diam nonummy nibh euismod tincidunt ut laoreet dolore magna aliquam erat volutpat. Ut wisi enim ad minim veniam, quis nostrud exerci tation ullamcorper suscipit lobortis nisl ut aliquip ex ea commodo consequat. Duis autem vel eum iriure dolor in hendrerit in vulputate velit esse molestie consequat, vel illum dolore eu feugiat.</p>
  <div class="btn blue" style="left:340px;top:734px;width:86px">Read More</div>
</section>

<!-- services -->
<section>
  <div class="abs services-band" role="img" aria-label="Overhead photo of students studying with laptops at a wooden table"></div>
  <h2 class="title" style="left:0;top:867px;width:1200px;text-align:center;color:#fff">Our Services</h2>
  <div class="divider" style="left:502px;top:916px;width:196px;background:#9a9a9a"></div>

  <svg class="arrow" style="left:106px" width="22" height="34" viewBox="0 0 22 34"><path d="M18 3L5 17l13 14" stroke="#fff" stroke-width="4" fill="none"/></svg>
  <svg class="arrow" style="left:1071px" width="22" height="34" viewBox="0 0 22 34"><path d="M4 3l13 14L4 31" stroke="#999" stroke-width="4" fill="none"/></svg>

  <div class="service-card orange" style="left:162px" role="img" aria-label="Open book emblem with live tutoring icon"></div>
  <div class="service-card grey" style="left:477px" role="img" aria-label="Open book emblem with online study icon"></div>
  <div class="service-card grey" style="left:795px" role="img" aria-label="Open book emblem with support agent icon"></div>

  <div class="service-title" style="left:134px">Live, One-On-One Tutoring</div>
  <div class="service-title" style="left:450px">Available 24/7 For Many Subjects</div>
  <div class="service-title" style="left:767px">Customized Service</div>

  <p class="service-text" style="left:164px">sit amet, consectetuer adipiscing elit, sed diam nonummy nsectetuer nibh euismod tincidunt</p>
  <p class="service-text" style="left:480px">sit amet, consectetuer adipiscing elit, sed diam nonummy nsectetuer nibh euismod tincidunt</p>
  <p class="service-text" style="left:797px">sit amet, consectetuer adipiscing elit, sed diam nonummy nsectetuer nibh euismod tincidunt</p>

  <div class="btn orange" style="left:242px;top:1302px;width:85px">Read More</div>
  <div class="btn blue" style="left:564px;top:1302px;width:86px">Read More</div>
  <div class="btn blue" style="left:875px;top:1302px;width:86px">Read More</div>
</section>

<!-- reviews -->
<section>
  <div class="abs reviews-bg"></div>
  <h2 class="title" style="left:0;top:1430px;width:1200px;text-align:center"><span class="o">Tutor's</span> <span class="b">Name Reviews</span></h2>
  <div class="divider" style="left:502px;top:1477px;width:196px"></div>
  <p class="abs reviews-sub">Tutors Name Has 2 Reviews With An Average Review Of 4.0</p>
  <table class="review-table">
    <colgroup><col style="width:258px"><col style="width:360px"><col style="width:258px"></colgroup>
    <tr><th>TUTEE NAME</th><th>DATE / TIME OF REVIEW</th><th>STAR RATEING 5.0</th></tr>
    <tr><td>Lorem Ipsum Dolor</td><td>Lorem Ipsum Dolor</td><td>85%</td></tr>
    <tr><td>Lorem Ipsum Dolor</td><td>Lorem Ipsum Dolor</td><td>85%</td></tr>
    <tr><td>Lorem Ipsum Dolor</td><td>Lorem Ipsum Dolor</td><td>85%</td></tr>
  </table>
  <div class="scroll"><i></i></div>
</section>

<!-- testimonial -->
<section>
  <h2 class="title" style="left:0;top:1783px;width:1200px;text-align:center"><span class="o">Client</span> <span class="b">Testimonial</span></h2>
  <div class="divider" style="left:502px;top:1831px;width:196px"></div>
  <svg class="quote" width="1200" height="2403" style="pointer-events:none">
    <path d="M174 1857 H1026 Q1038 1857 1038 1869 V1922 Q1038 1934 1026 1934 H310 L306 1989 L290 1934 H174 Q162 1934 162 1922 V1869 Q162 1857 174 1857 Z" fill="#fff" stroke="#cfcfcf" stroke-width="1.3"/>
  </svg>
  <p class="abs quote-text">Lorem ipsum dolor sit amet, consectetuer adipiscing elit, sed diam nonummy nibh euismod tincidunt ut laoreet dolore magna aliquam erat volutpat. Ut wisi enim ad minim veniam, quis nostrud exerci tation ullamcorper suscipit lobortis nisl ut aliquip ex ea commodo consequat. Duis autem vel eum iriure dolor in hendrerit in vulputate velit esse molestie consequat, vel illum dolore eu</p>
  <div class="abs avatar" role="img" aria-label="Client portrait"></div>
  <div class="abs client-name">Lorem Ipsum Dolor</div>
  <div class="abs client-city">New York</div>
</section>

<!-- footer -->
<footer class="abs footer">
  <div class="f-head" style="left:162px;width:95px">Quick Link</div>
  <div class="f-head" style="left:328px;width:167px">Contact Info</div>
  <div class="f-head" style="left:569px;width:216px">Quick Contact</div>

  <span class="f-link" style="top:97px">Home</span>
  <span class="f-link" style="top:127px">About</span>
  <span class="f-link" style="top:157px">Student</span>
  <span class="f-link" style="top:187px">Tutor</span>
  <span class="f-link" style="top:217px">Contact</span>

  <p class="f-text" style="top:97px">Lend Your Lessons<br>Lorem ipsum dolor sit amet,<br>consectetuer adipiscing elit<br>1234</p>
  <div class="f-icon" style="top:173px">
    <svg width="13" height="13" viewBox="0 0 24 24"><path fill="#fff" d="M6.6 10.8a15.1 15.1 0 0 0 6.6 6.6l2.2-2.2c.3-.3.7-.4 1-.2 1.1.4 2.3.6 3.6.6.6 0 1 .4 1 1V20c0 .6-.4 1-1 1A17 17 0 0 1 3 4c0-.6.4-1 1-1h3.5c.6 0 1 .4 1 1 0 1.3.2 2.5.6 3.6.1.3 0 .7-.2 1z"/></svg>
    <span>123 456 7890</span>
  </div>
  <div class="f-icon" style="top:207px;font-size:11.5px">
    <svg width="14" height="10" viewBox="0 0 20 14"><rect x="0.5" y="0.5" width="19" height="13" fill="#fff"/><path d="M1 1l9 7 9-7" stroke="#323232" stroke-width="1.5" fill="none"/></svg>
    <span>info@lendyourlessons.com</span>
  </div>

  <div class="f-input" style="top:91px;height:26px">Name</div>
  <div class="f-input" style="top:126px;height:26px">Email</div>
  <div class="f-input" style="top:160px;height:56px">Message</div>
  <div class="f-submit">Submit</div>

  <div class="f-brand-mark"></div>
  <div class="f-brand">LendYourLessons</div>
</footer>

<!-- bottom bar -->
<div class="abs bottombar">
  <span class="abs" style="left:162px;top:14px">Copyright 16. Lend Your Lessons. All Right Reserved.</span>
  <span class="abs" style="left:833px;top:14px;font-size:11.5px">Follow Us</span>
  <span class="social on" style="left:899px"></span>
  <span class="social" style="left:935px"></span>
  <span class="social" style="left:972px"></span>
  <span class="social" style="left:1009px"></span>
</div>

</body>
</html>
```